nutrition ebook cover

i need a cover for a ebook designed, the book is called Amber Lattice so i would like that somewhere on the cover. i would also like the word nutrition followed by my company logo that i have attached below somewhere on the cover( i have attached two logos and would like to see with both separatley), i would like this to be faded into the background if possible, perhaps in a upper or lower corner. i would also like to see options with and without the picture i have attached below. the look I'm going for is professional and clean. this is a fat loss, healthy eating booklet. the winning designer i would like to design the following pages within the book aswell no more than 10 pages, that i will provide all content for, i just need help with putting what i have on pdf in a way that looks professional and cool. this would ideally covered in the rate that is paid for the cover. i also have other booklets i need made so the winning designer will most likely get that work too at a later date for an additional fee of course.

Industry/Entity Type

Nutrition

Requirements
Nice to have
• Outside images are welcomed, happy to purchase any stock images used from a outside source

```html
<!DOCTYPE html>
<html lang="en">
<head>
<meta charset="utf-8">
<title>Amber Lattice — ebook cover</title>
<link rel="stylesheet" href="https://fonts.googleapis.com/css2?family=Bebas+Neue&family=Libre+Caslon+Text&display=swap">
<style>
  :root {
    --slate-dark: #16262b;
    --slate: #243a40;
    --wood-dark: #5a2a16;
    --wood: #8a3c1c;
    --wood-glow: #c4582a;
    --ink-white: #ffffff;
    --mark-grey: #7d7d7b;
    --badge-fill: rgba(236, 234, 228, 0.72);
    --faded-white: rgba(255, 255, 255, 0.28);
  }
  html, body {
    margin: 0;
    padding: 0;
    overflow: hidden;
    background: var(--slate-dark);
  }
  .cover {
    position: relative;
    width: 800px;
    height: 1200px;
    overflow: hidden;
  }
  .cover-photo {
    position: absolute;
    inset: 0;
    background:
      radial-gradient(ellipse 60% 45% at 78% 62%, var(--wood-glow) 0%, var(--wood) 38%, var(--wood-dark) 70%, transparent 100%),
      linear-gradient(100deg, var(--slate-dark) 0%, var(--slate) 40%, var(--wood-dark) 62%, var(--wood) 100%);
  }
  .brand-badge {
    position: absolute;
    left: 448px;
    top: 64px;
    width: 244px;
    height: 244px;
    display: flex;
    align-items: center;
    justify-content: center;
  }
  .brand-badge__disc {
    position: absolute;
    inset: 0;
    border-radius: 50%;
    background: var(--badge-fill);
  }
  .brand-badge__name {
    position: relative;
    font-family: "Bebas Neue", sans-serif;
    font-size: 44px;
    line-height: 0.95;
    letter-spacing: 2px;
    text-align: center;
    color: var(--mark-grey);
  }
  .title {
    position: absolute;
    right: 32px;
    top: 404px;
    text-align: right;
    color: var(--ink-white);
  }
  .title__main {
    display: block;
    font-family: "Bebas Neue", sans-serif;
    font-size: 290px;
    line-height: 0.9;
    letter-spacing: 2px;
  }
  .title__sub {
    display: block;
    margin-top: 6px;
    font-family: "Libre Caslon Text", serif;
    font-size: 108px;
    line-height: 1;
  }
  .brand-faded {
    position: absolute;
    right: 40px;
    top: 930px;
    font-family: "Bebas Neue", sans-serif;
    font-size: 130px;
    line-height: 1;
    letter-spacing: 2px;
    color: var(--faded-white);
  }
</style>
</head>
<body>
  <main class="cover">
    <div class="cover-photo" role="img" aria-label="Top-down photo of fresh vegetables — potatoes, spring onion, mushrooms, chillies, peppercorns, a turnip and rocket — around a worn wooden chopping board on a dark slate surface"></div>

    <div class="brand-badge">
      <span class="brand-badge__disc"></span>
      <span class="brand-badge__name">Kestrel<br>Fitness</span>
    </div>

    <h1 class="title">
      <span class="title__main">Amber</span>
      <span class="title__sub">Lattice</span>
    </h1>

    <div class="brand-faded">Kestrel</div>
  </main>
</body>
</html>
```